Book a car wash

The app will have a logo, contact details and address
It will then lead you to booking a service from list
The customer will have a date, day and time

Booking - There are two types of times arrival is the main - day, date, time, service, payment. Each car takes and average of 1.5 hours

Pay by qfund or cashlyn or merchant

List of services
Bronze $25
Silver $40
Gold $55
Leather Plus $90
Diamond $100
Ruby $100
Standard Vehicle $0
Larger Vehicle & 4wd $10

Target Market(s)

Professionals with time issues
Parents with time management concerns

Industry/Entity Type

It Service

Requirements
Must have
• Logo
Menu list
Payment system
Address and contact details
Basement CarPark - Winsley Arcade Shopping Centre
Tolvane rd, Claremont
0493527641
Nice to have
• Big fonts and step by step process
Should not have
• No cars or washing items i.e. sponges

```html
<!DOCTYPE html>
<html lang="en">
<head>
<meta charset="utf-8">
<title>Park &amp; Shine – Welcome Screen</title>
<link rel="stylesheet" href="https://fonts.googleapis.com/css2?family=Cardo:wght@400;700&family=Arimo:wght@400;700&display=swap">
<style>
  :root{
    --bg:#252525;
    --ink-light:#ffffff;
    --ink-dark:#3a3a3a;
    --brand-red:#d02a2a;
    --tile-top:#ffffff;
    --tile-bottom:#dcdcdc;
    --bar-dark:#2b2b2b;
    --bar-cell:#363636;
    --bar-active:#232323;
    --bar-text:#c9c9c9;
    --accent-blue:#29b6f6;
    --status:#000000;
  }
  *{box-sizing:border-box;margin:0;padding:0}
  html,body{width:1200px;height:1000px;overflow:hidden;background:var(--bg)}
  .canvas{position:relative;width:1200px;height:1000px;background:var(--bg);font-family:"Cardo",Georgia,serif;color:var(--ink-light)}

  .headline{position:absolute;left:133px;top:304px;font-size:68px;font-weight:700;line-height:1;white-space:nowrap}
  .subline{position:absolute;left:120px;top:424px;font-size:56px;font-weight:700;line-height:1;white-space:nowrap}
  .subline .chev{margin-left:14px;letter-spacing:4px}

  .app-icon{position:absolute;left:232px;top:648px;width:160px;height:160px;border-radius:30px;
    background:linear-gradient(#f4f4f4,#cfcfcf);display:flex;align-items:center;justify-content:center}
  .app-icon .name{color:var(--ink-dark);font-size:24px;font-weight:400;white-space:nowrap}

  .screen{position:absolute;left:655px;top:190px;width:325px;height:575px;overflow:hidden;background:var(--brand-red)}
  .status-bar{height:22px;background:var(--status);font-family:"Arimo",Arial,sans-serif;font-size:12px;font-weight:700;color:#fff;
    display:flex;align-items:center;justify-content:space-between;padding:0 8px}
  .status-bar .carrier{display:flex;align-items:center;gap:4px}
  .body{position:relative;height:500px;background:var(--brand-red)}
  .title{position:absolute;top:36px;width:100%;text-align:center;line-height:1}
  .title .main{font-size:28px;display:block}
  .title .place{font-size:22px;display:block;margin-top:4px}
  .title .area{font-size:13px;letter-spacing:6px;display:block;margin-top:8px}
  .logo-tile{position:absolute;left:63px;top:162px;width:195px;height:197px;border-radius:4px;
    background:linear-gradient(var(--tile-top),var(--tile-bottom));box-shadow:0 2px 4px rgba(0,0,0,.35);
    display:flex;align-items:center;justify-content:center}
  .logo-tile .name{color:var(--ink-dark);font-size:27px;font-weight:400;white-space:nowrap}
  .book-btn{position:absolute;left:62px;top:433px;width:198px;height:35px;border-radius:3px;
    background:linear-gradient(#ffffff,#d4d4d4);box-shadow:0 1px 3px rgba(0,0,0,.4);
    font-family:"Arimo",Arial,sans-serif;font-size:16px;color:#1b1b1b;display:flex;align-items:center;justify-content:center}
  .tab-bar{display:flex;height:53px;background:var(--bar-dark)}
  .tab{flex:1;display:flex;flex-direction:column;align-items:center;justify-content:flex-end;padding-bottom:6px;gap:4px;
    background:var(--bar-cell);border-right:1px solid #222;font-family:"Arimo",Arial,sans-serif;font-size:9px;color:var(--bar-text);position:relative}
  .tab.active{background:var(--bar-active);flex:1.25}
  .tab.active::before{content:"";position:absolute;top:4px;left:25%;width:50%;height:3px;border-radius:2px;background:var(--accent-blue)}
  .tab svg{width:22px;height:22px;fill:none;stroke:#8a8a8a;stroke-width:2}
</style>
</head>
<body>
<div class="canvas">
  <h1 class="headline">Park &amp; Shine</h1>
  <p class="subline">Welcome Screen<span class="chev">››</span></p>

  <div class="app-icon" aria-label="Park &amp; Shine app icon">
    <span class="name">Park &amp; Shine</span>
  </div>

  <div class="screen">
    <div class="status-bar">
      <span class="carrier">
        <svg width="18" height="10" viewBox="0 0 18 10" fill="#fff"><rect x="0" y="7" width="2" height="3"/><rect x="4" y="5" width="2" height="5"/><rect x="8" y="3" width="2" height="7"/><rect x="12" y="1" width="2" height="9"/></svg>
        Telvo
      </span>
      <span class="time">4:20 PM</span>
      <svg width="24" height="11" viewBox="0 0 24 11"><rect x=".5" y=".5" width="20" height="10" rx="2" fill="none" stroke="#fff"/><rect x="2" y="2" width="17" height="7" fill="#fff"/><rect x="21" y="3.5" width="2" height="4" fill="#fff"/></svg>
    </div>

    <div class="body">
      <div class="title">
        <span class="main">PARK &amp; SHINE</span>
        <span class="place">WINSLEY</span>
        <span class="area">ARCADE</span>
      </div>
      <div class="logo-tile">
        <span class="name">Park &amp; Shine</span>
      </div>
      <div class="book-btn">Make a Booking</div>
    </div>

    <nav class="tab-bar">
      <div class="tab"><svg viewBox="0 0 22 22"><path d="M3 11 L11 3 L19 11 M6 9 V19 H16 V9"/></svg>Home</div>
      <div class="tab"><svg viewBox="0 0 22 22"><path d="M3 5h3M9 5h10M3 11h3M9 11h10M3 17h3M9 17h10"/></svg>Services</div>
      <div class="tab active"><svg viewBox="0 0 22 22"><path d="M4 8h14M4 13h14M4 18h14"/></svg>Booking</div>
      <div class="tab"><svg viewBox="0 0 22 22"><circle cx="11" cy="7" r="4"/><path d="M3 20c1-5 4-7 8-7s7 2 8 7"/></svg>info</div>
      <div class="tab"><svg viewBox="0 0 22 22"><path d="M4 18 L6 13 L16 3 L19 6 L9 16 Z"/></svg>Contact</div>
    </nav>
  </div>
</div>
</body>
</html>
```